Elegant and modern Wedding Photography brochure

My existing brochure (attached) needs a major facelift. This is one of the main selling tools - it gets emailed to my clients when they make an equiry on what packages i offer and it is printed out and walked through at our first meeting. This brochure is as critical as my website - it needs to sing!

I'm looking for an eye-catching design that says:
Elegant
Modern
Clean
Crisp
Not cutesy or lovey-dovey thanks - we are more sophisticated and professional than that.

Update images to some of the latest weddings I've shot also. Let me know files and resolution you need. I've enabled right-click to download images on my site for a limited time. Please note that I retain copyright and will pursue any breeches.

Http://www.carlathornbey.com/Melbourne-wedding-photography
Updates

Thanks for all of your designs! Will take a few days to decide.

Target Market(s)

Australian Women aged 24-44

Industry/Entity Type

Wedding

Font styles to use
Other font styles liked:
• Century Gothic

Requirements
Must have
• Easy to print - does not have to be 6 A4 pages like the existing brochure
Nice to have
• Some full page images - The photos are supposed to be the hero here :-)
Should not have
• Not cutesy or lovey-dovey thanks - we are more sophisticated and professional than that.

No black backgrounds, I prefer a white thanks

No images in organic shaped boxes (like the rectangles in the logo - no thanks).
Keep the lines straight and sharp

```html
<!DOCTYPE html>
<html lang="en">
<head>
<meta charset="utf-8">
<title>Carla's approach – Wedding Photography Brochure</title>
<link rel="stylesheet" href="https://fonts.googleapis.com/css2?family=Questrial&family=Mulish:wght@800&display=swap">
<style>
  :root {
    --page-bg: #ffffff;
    --violet: #8a1ee8;
    --violet-soft: #b77ee6;
    --ink: #141010;
    --panel: rgba(236, 232, 220, 0.62);
    --photo-light: #c9bfa4;
    --photo-mid: #8c7a5c;
    --photo-dark: #2a2016;
  }
  * { margin: 0; padding: 0; box-sizing: border-box; }
  html, body {
    width: 1200px;
    height: 1000px;
    overflow: hidden;
    background: var(--page-bg);
  }
  .spread {
    position: absolute;
    left: 180px;
    top: 203px;
    width: 842px;
    height: 595px;
    overflow: hidden;
  }
  .hero-photo {
    position: absolute;
    inset: 0;
    background:
      radial-gradient(ellipse 45% 55% at 62% 48%, rgba(214, 206, 180, 0.9), rgba(214, 206, 180, 0) 70%),
      linear-gradient(180deg, rgba(42, 32, 22, 0.55) 0%, rgba(42, 32, 22, 0) 35%, rgba(42, 32, 22, 0) 70%, rgba(42, 32, 22, 0.7) 100%),
      linear-gradient(90deg, var(--photo-dark) 0%, var(--photo-mid) 18%, var(--photo-light) 50%, var(--photo-mid) 80%, var(--photo-dark) 100%);
  }
  .hero-title {
    position: absolute;
    left: 12px;
    top: 330px;
    font-family: "Questrial", "Century Gothic", sans-serif;
    color: var(--violet);
  }
  .hero-title h1 {
    font-weight: 400;
    font-size: 44px;
    letter-spacing: 3px;
    line-height: 1;
  }
  .hero-title p {
    font-size: 20px;
    letter-spacing: 2.4px;
    color: var(--violet-soft);
    margin-top: 6px;
  }
  .info-panel {
    position: absolute;
    left: 451px;
    top: 23px;
    width: 373px;
    height: 555px;
    background: var(--panel);
    padding: 14px 20px 0 22px;
  }
  .info-block { margin-bottom: 22px; }
  .info-block h2 {
    font-family: "Questrial", "Century Gothic", sans-serif;
    font-weight: 400;
    -webkit-text-stroke: 0.5px var(--violet);
    font-size: 14.5px;
    letter-spacing: 2px;
    color: var(--violet);
    margin-bottom: 5px;
  }
  .info-block p {
    font-family: "Mulish", "Century Gothic", sans-serif;
    font-weight: 800;
    font-size: 10px;
    line-height: 14px;
    letter-spacing: 0.9px;
    text-align: justify;
    color: var(--ink);
  }
</style>
</head>
<body>
  <main class="spread">
    <div class="hero-photo" role="img" aria-label="Sepia-toned photo of a bride in a short dotted dress and a groom in a dark suit kissing beneath large park trees"></div>

    <header class="hero-title">
      <h1>Carla’s approach</h1>
      <p>Enjoy your special day!</p>
    </header>

    <section class="info-panel">
      <article class="info-block">
        <h2>Style &amp; Approach</h2>
        <p>Carla can observe and capture your wedding day in the background, quickly and quietly taking photojournalistic pictures rather than directing it if you prefer. Or she can confidently play the role of Art Director and instruct beautiful poses. Either way, what is most important is that her clients are relaxed and having a really great time on their wedding day!</p>
      </article>
      <article class="info-block">
        <h2>Formal Photography</h2>
        <p>Many of Carla's clients book her because of the easy-going approach she has. They can get on with having a great time on their day without worrying about formal photography. However, there are occasions when clients do want formal family pictures, and Carla is more than happy to accommodate their requests. In order to keep the disruption on the day to a minimum, we recommend that Carla photographs no more than 6 groups, and a select number of the special couple.</p>
      </article>
      <article class="info-block">
        <h2>Image Presentation</h2>
        <p>The most professional way of presenting clients with their photographs is in an elegantly designed photo book. Carla's clients only pay one fixed price for the photography, regardless of how many images taken. There are no hard sell procedures to go through, and the completed book is prepared within 2-6 weeks after the wedding day.</p>
      </article>
      <article class="info-block">
        <h2>Time of Year</h2>
        <p>Signature pictures can be taken on overcast days or winter months. Don't worry if the sky is not perfectly blue. In the end, regardless of the weather – it's the timeless mood of the day that Carla strives to capture.</p>
      </article>
    </section>
  </main>
</body>
</html>
```